Business Card Design Project

We are an incubator company that helps young entrepreneur to launch new ideas into the market. We will be targeting investors or likewise; Angels, young entrepreneurs and technopreneurs.

Our logo is being tasked by artswarm to design, therefore there is no logo for now.
You can us Lanternfield Pte Ltd as the logo for the time being.

Please let us have some versions of modern and yet professional designs; for words, you can indicate e.g (address), (Title)

thanks

Target Market(s)

young entrepreneurs
angels, investors

Industry/Entity Type

Business

Colors
3176b5
ffffff

Requirements
Must have
• able to project out our name; Lanternfield
Should not have
• Nothing childish or cartoon

```html
<!DOCTYPE html>
<html lang="en">
<head>
<meta charset="utf-8">
<title>Lanternfield Pte Ltd — Business Card</title>
<link rel="stylesheet" href="https://fonts.googleapis.com/css2?family=Mulish:wght@300;400;800&display=swap">
<style>
  :root {
    --backdrop: #5f6063;
    --card-blue: #1b9fe1;
    --card-white: #ffffff;
  }
  * { margin: 0; padding: 0; box-sizing: border-box; }
  html, body {
    width: 1200px;
    height: 910px;
    overflow: hidden;
    background: var(--backdrop);
  }
  .card {
    position: absolute;
    left: 75px;
    top: 155px;
    width: 1050px;
    height: 600px;
    background: var(--card-blue);
    color: var(--card-white);
    font-family: "Mulish", sans-serif;
    overflow: hidden;
  }
  .identity {
    position: absolute;
    left: 400px;
    top: 160px;
  }
  .identity__name {
    font-size: 46px;
    font-weight: 300;
    letter-spacing: 0.5px;
    line-height: 1;
  }
  .identity__name strong { font-weight: 800; }
  .identity__title {
    margin-top: 8px;
    font-size: 24px;
    font-weight: 300;
    letter-spacing: 0.5px;
  }
  .contact {
    position: absolute;
    left: 400px;
    top: 300px;
    list-style: none;
    font-size: 17px;
    font-weight: 300;
    line-height: 1.45;
    letter-spacing: 0.4px;
  }
  .brand-name {
    position: absolute;
    right: 22px;
    top: 18px;
    writing-mode: vertical-rl;
    font-size: 74px;
    font-weight: 800;
    letter-spacing: 1px;
    line-height: 1;
  }
  .corner-mark {
    position: absolute;
    left: -40px;
    bottom: -110px;
    width: 280px;
    height: 280px;
  }
</style>
</head>
<body>
  <section class="card">
    <div class="identity">
      <h1 class="identity__name">Your<strong>Name</strong></h1>
      <p class="identity__title">designation</p>
    </div>
    <ul class="contact">
      <li>Phone:</li>
      <li>Email:</li>
      <li>Fax:</li>
      <li>Address:</li>
    </ul>
    <div class="brand-name">lanternfield</div>
    <svg class="corner-mark" viewBox="0 0 280 280" role="img" aria-label="White corner circle with a decorative circuit-line motif">
      <circle cx="140" cy="140" r="140" fill="var(--card-white)"/>
    </svg>
  </section>
</body>
</html>
```